NEED VIBRANT DIGTAL MENUS

NEED A NEW DESIGN FOR MENU SCREENS

SEE ATTACHED FOR EXISTING MENUS

Requirements
Must have
• FLOW. COLOR. ORGANIZATION. SOPHISTICATION.
Nice to have
• INCORPORATE LOGO IN DESIGNS

```html
<!DOCTYPE html>
<html lang="en">
<head>
<meta charset="utf-8">
<title>Breakfast Menu</title>
<link rel="stylesheet" href="https://fonts.googleapis.com/css2?family=Abril+Fatface&family=Fira+Sans:wght@800&family=Fira+Sans+Condensed:wght@700&display=swap">
<style>
  :root {
    --sun: #ffe600;
    --sun-deep: #ffc400;
    --amber: #ffb300;
    --ink: #0a0a0a;
    --chili: #f20d0d;
    --bun-light: #eaa64a;
    --bun: #d98a2b;
    --plate: #e9e4dc;
    --plate-warm: #d8c4a4;
  }
  * { margin: 0; padding: 0; box-sizing: border-box; }
  html, body { width: 1200px; height: 674px; overflow: hidden; }
  body { background: var(--sun); }
  .menu-screen {
    position: relative;
    width: 1200px;
    height: 674px;
    overflow: hidden;
    background: linear-gradient(180deg, var(--sun-deep) 0%, var(--sun) 45%, #fff200 100%);
  }
  .texture {
    position: absolute;
    border-radius: 50%;
    filter: blur(18px);
    opacity: .55;
  }
  .texture--top { left: -40px; top: -40px; width: 620px; height: 150px;
    background: linear-gradient(100deg, var(--amber), rgba(255,196,0,0)); transform: rotate(-8deg); }
  .texture--bottom { left: -30px; top: 585px; width: 620px; height: 140px;
    background: linear-gradient(80deg, var(--amber), rgba(255,196,0,0)); transform: rotate(-6deg); }
  .title-echo {
    position: absolute;
    left: 180px; top: -10px;
    font-family: "Abril Fatface", serif;
    font-size: 170px;
    line-height: 1;
    color: rgba(255,255,255,.16);
    white-space: nowrap;
  }
  .title {
    position: absolute;
    left: 318px; top: 28px;
    font-family: "Abril Fatface", serif;
    font-size: 112px;
    line-height: 1;
    color: var(--ink);
    letter-spacing: 1px;
  }
  .swoosh { position: absolute; left: 0; top: 0; }
  .menu-list {
    position: absolute;
    left: 77px; top: 192px;
    list-style: none;
  }
  .menu-item {
    display: flex;
    align-items: baseline;
    height: 42.7px;
    font-family: "Fira Sans", sans-serif;
    font-weight: 800;
    font-size: 20px;
    letter-spacing: 1.5px;
    color: var(--ink);
    white-space: nowrap;
  }
  .menu-item::before {
    content: "";
    flex: none;
    width: 9px; height: 9px;
    border-radius: 50%;
    background: var(--chili);
    margin-right: 15px;
    transform: translateY(-5px);
  }
  .price {
    font-family: "Fira Sans Condensed", sans-serif;
    font-weight: 700;
    font-size: 31px;
    letter-spacing: .5px;
    color: var(--chili);
    margin-left: 8px;
  }
  .hero-photo {
    position: absolute;
    left: 712px; top: 132px;
    width: 462px; height: 356px;
    border-radius: 46% 46% 26% 26% / 50% 50% 30% 30%;
    background: linear-gradient(180deg, var(--bun-light) 0%, var(--bun) 100%);
  }
  .side-photo {
    position: absolute;
    left: 922px; top: 446px;
    width: 193px; height: 193px;
    border-radius: 50%;
    background: radial-gradient(circle, var(--plate-warm) 0%, var(--plate) 100%);
  }
</style>
</head>
<body>
<main class="menu-screen">
  <div class="texture texture--top" aria-hidden="true"></div>
  <div class="texture texture--bottom" aria-hidden="true"></div>
  <div class="title-echo" aria-hidden="true">Breakfast</div>
  <h1 class="title">Breakfast</h1>
  <svg class="swoosh" width="1200" height="674" aria-hidden="true">
    <path d="M297 170 C 500 160, 720 148, 886 143 C 760 156, 520 168, 297 171 Z" fill="var(--chili)"/>
  </svg>
  <ul class="menu-list">
    <li class="menu-item">BACON, EGG, &amp; CHEESE <span class="price">$4.29</span></li>
    <li class="menu-item">SAUSAGE, EGG &amp; CHEESE <span class="price">$4.29</span></li>
    <li class="menu-item">HAM, EGG &amp; CHEESE <span class="price">$5.49</span></li>
    <li class="menu-item">STEAK, EGG &amp; CHEESE <span class="price">$7.49</span></li>
    <li class="menu-item">CHICKEN EGG, &amp; CHEESE <span class="price">$6.99</span></li>
    <li class="menu-item">BOLOGNA, EGG, &amp; CHEESE <span class="price">$5.99</span></li>
    <li class="menu-item">CLASSIC BLT <span class="price">$5.29</span></li>
    <li class="menu-item">SAUSAGE, EGG &amp; CHEESE OR BACON EGG &amp; CHEESE <span class="price">$4.89</span></li>
    <li class="menu-item">BACON, SAUSAGE, EGG &amp; CHEESE <span class="price">$6.49</span></li>
    <li class="menu-item">BREAKFAST PLATTER <span class="price">$6.99</span></li>
  </ul>
  <div class="hero-photo" role="img" aria-label="Photo of a breakfast burger with bacon, fried egg, tomato, lettuce and melted cheese on a brioche bun"></div>
  <div class="side-photo" role="img" aria-label="Photo of a sausage, egg and cheese sandwich on an English muffin"></div>
</main>
</body>
</html>
```